Digital Asset Exchange (Trading Platform)

We need a design of Digital Asset Exchange Trading Platform.

Please find attached a mock up of VelmoraTrade design this has to be redesigned based on plinor.co.uk style.

Industry/Entity Type

Digital

```html
<!DOCTYPE html>
<html lang="en">
<head>
<meta charset="utf-8">
<title>VelmoraTrade</title>
<link rel="stylesheet" href="https://fonts.googleapis.com/css2?family=Open+Sans:wght@400;600;700&family=Exo+2:wght@400;500&family=Tinos&family=Arimo:wght@400;700&display=swap">
<style>
:root{
  --dark:#333333;
  --darker:#2a2a2a;
  --orange:#f08a12;
  --orange-deep:#c65f05;
  --ink:#444444;
  --muted:#777777;
  --pale:#f6f6f6;
  --line:#e2e2e2;
  --white:#ffffff;
}
*{margin:0;padding:0;box-sizing:border-box}
html,body{width:668px;height:1200px;overflow:hidden}
body{position:relative;background:var(--white);font-family:"Arimo",Arial,sans-serif;color:var(--ink)}
.abs{position:absolute}

.site-header{left:0;top:0;width:668px;height:70px;background:var(--dark)}
.brand{left:56px;top:20px;display:flex;align-items:center;gap:8px}
.brand-dot{width:30px;height:30px;border-radius:50%;background:var(--orange)}
.brand-name{font-family:"Open Sans",sans-serif;font-size:18px;font-weight:400;color:var(--white)}
.main-nav{top:37px;left:0;font-family:"Arimo",sans-serif;font-size:10.5px;color:var(--white)}
.main-nav span{position:absolute;white-space:nowrap}
.main-nav .active{color:var(--orange)}

.hero{left:0;top:70px;width:668px;height:266px;background:radial-gradient(circle at 30% 20%,#f39a26,#e07a0a 45%,#b55a08 100%)}
.hero-title{top:86px;width:668px;text-align:center;font-family:"Open Sans",sans-serif;font-size:24px;color:var(--white);text-shadow:0 1px 2px rgba(0,0,0,.3)}
.hero-media{left:126px;top:128px;width:432px;height:256px;border-radius:8px;background:linear-gradient(180deg,#d9e6f3 0%,#b9cde0 70%,#c9c9cb 100%)}

.feature{top:414px;width:196px;text-align:center}
.feature-icon{width:52px;height:52px;margin:0 auto;border-radius:50%;background:#eeeeee;display:flex;align-items:center;justify-content:center}
.feature-icon i{width:40px;height:40px;border-radius:50%;background:var(--orange);display:flex;align-items:center;justify-content:center}
.feature-title{margin-top:16px;font-family:"Exo 2",sans-serif;font-size:12px;color:#333}
.feature-title em{font-style:normal;color:var(--orange)}
.feature-text{margin-top:12px;font-size:7px;line-height:11px;color:var(--muted)}

.band{left:0;top:564px;width:668px;height:456px;background:var(--pale)}
.section-title{font-family:"Open Sans",sans-serif;font-size:15px;font-weight:600;color:var(--ink);letter-spacing:.2px}
.stat{font-family:"Open Sans",sans-serif;font-size:9.5px;color:#333}
.tabs{left:78px;top:639px;display:flex}
.tabs span{border:1px solid #dddddd;background:#eeeeee;font-size:6.5px;color:#777;padding:3px 6px;margin-right:-1px}
.tabs .on{background:#d98b0a;color:var(--white);border-color:#d98b0a}
.chart{left:56px;top:654px}

.news{left:414px;width:196px}
.news-photo{width:48px;height:38px;border:2px solid var(--white);box-shadow:0 0 2px rgba(0,0,0,.25);background:linear-gradient(135deg,#8fb4d9,#dcc2a7)}
.news-date{font-size:6px;color:var(--orange)}
.news-head{font-family:"Exo 2",sans-serif;font-size:8.5px;font-weight:500;color:var(--orange)}
.news-text{font-size:6.5px;line-height:10px;color:#555}
.news-more{font-size:6px;color:#333}
.cal{display:inline-block;width:9px;height:9px;border:1px solid #4a6fa5;border-top-width:3px;margin-right:8px;vertical-align:-2px;background:var(--white)}

.quote{top:897px;width:172px;height:45px;background:var(--white);border:1px solid #e6e6e6;padding:8px 6px;font-family:"Tinos",serif;font-size:7px;line-height:12px;color:#444}
.quote::after{content:"";position:absolute;left:18px;bottom:-7px;width:12px;height:12px;background:var(--white);border-right:1px solid #e6e6e6;border-bottom:1px solid #e6e6e6;transform:rotate(45deg)}
.avatar{width:32px;height:32px;border-radius:50%;background:linear-gradient(135deg,#c9a58a,#6d5546)}
.reviewer{font-size:6.5px;color:#666}

.site-footer{left:0;top:1020px;width:668px;height:144px;background:var(--dark)}
.foot-col{top:1047px}
.foot-col h4{font-family:"Arimo",sans-serif;font-size:10px;font-weight:700;color:var(--white);padding-bottom:5px;border-bottom:1px solid #4a4a4a;width:72px}
.foot-col ul{list-style:none;margin-top:9px}
.foot-col li{font-size:7.5px;color:#8a8a8a;line-height:13.3px}
.social-note{font-size:6.5px;line-height:11px;color:#8a8a8a;width:170px;margin-top:9px}
.social{left:429px;top:1107px;display:flex;gap:6px}
.social i{width:18px;height:18px;background:#262626;border-radius:2px}
.social .hot{background:var(--orange)}
.legal{left:0;top:1164px;width:668px;height:36px;background:var(--darker);text-align:center;font-size:7px;color:#8a8a8a;line-height:36px}
</style>
</head>
<body>

<header class="abs site-header">
  <div class="abs brand"><span class="brand-dot"></span><span class="brand-name">VelmoraTrade</span></div>
  <nav class="abs main-nav">
    <span class="active" style="left:377px">Home</span>
    <span style="left:423px">Features</span>
    <span style="left:482px">Security</span>
    <span style="left:537px">Support</span>
  </nav>
</header>

<section class="abs hero"></section>
<h1 class="abs hero-title" style="font-weight:400">Simple Investing Prosperous Future</h1>
<div class="abs hero-media" role="img" aria-label="Laptop showing an explainer video titled What is Bitcoin over a rising price chart"></div>

<div class="abs feature" style="left:29px">
  <div class="feature-icon"><i><svg width="14" height="14" viewBox="0 0 14 14"><rect x="3" y="6" width="8" height="6" fill="#fff"/><path d="M4.5 6V4a2.5 2.5 0 0 1 5 0v2" fill="none" stroke="#fff" stroke-width="1.5"/></svg></i></div>
  <div class="feature-title"><em>About</em> Bitcoin</div>
  <p class="feature-text">simply dummy text of the printing and typesetting industry. Lorem Ipsum has been the industry's standard dummy text ever since the 1500s, when</p>
</div>
<div class="abs feature" style="left:224px">
  <div class="feature-icon"><i><svg width="16" height="14" viewBox="0 0 16 14"><path d="M8 1l3 3H9v3H7V4H5z" fill="#fff"/><rect x="2" y="8" width="12" height="4" fill="#fff"/></svg></i></div>
  <div class="feature-title"><em>How to</em> My Buy</div>
  <p class="feature-text">simply dummy text of the printing and typesetting industry. Lorem Ipsum has been the industry's standard dummy text ever since the 1500s, when</p>
</div>
<div class="abs feature" style="left:414px">
  <div class="feature-icon"><i><svg width="16" height="16" viewBox="0 0 16 16" stroke="#fff" fill="#fff"><line x1="8" y1="8" x2="3" y2="3"/><line x1="8" y1="8" x2="13" y2="3"/><line x1="8" y1="8" x2="3" y2="13"/><line x1="8" y1="8" x2="13" y2="13"/><circle cx="8" cy="8" r="2"/><circle cx="3" cy="3" r="1.3"/><circle cx="13" cy="3" r="1.3"/><circle cx="3" cy="13" r="1.3"/><circle cx="13" cy="13" r="1.3"/></svg></i></div>
  <div class="feature-title"><em>How to</em> Sell</div>
  <p class="feature-text">simply dummy text of the printing and typesetting industry. Lorem Ipsum has been the industry's standard dummy text ever since the 1500s, when</p>
</div>

<section class="abs band"></section>

<h2 class="abs section-title" style="left:67px;top:593px">MARKET OVERVIEW</h2>
<div class="abs stat" style="left:68px;top:618px">Market Cap: $5,183,441,043.00</div>
<div class="abs stat" style="left:271px;top:618px">Total BTC: 12,626,525 BTC</div>
<div class="abs tabs"><span class="on">1m</span><span>3m</span><span>6m</span><span>YTD</span><span>1y</span><span>All</span></div>

<svg class="abs chart" width="340" height="166" viewBox="0 0 340 166" font-family="Arimo, sans-serif" font-size="6" fill="#999">
  <rect x="22" y="0" width="316" height="144" fill="#ffffff"/>
  <g stroke="#d8d8d8" stroke-width="1">
    <line x1="22" y1="28" x2="338" y2="28"/><line x1="22" y1="57" x2="338" y2="57"/>
    <line x1="22" y1="87" x2="338" y2="87"/><line x1="22" y1="116" x2="338" y2="116"/>
  </g>
  <polygon points="22,82 30,78 40,84 67,72 84,77 112,57 134,46 142,53 154,48 187,82 207,82 227,97 242,90 270,99 292,70 312,70 322,87 332,76 338,72 338,144 22,144" fill="#fbe8c4"/>
  <polyline points="22,82 30,78 40,84 67,72 84,77 112,57 134,46 142,53 154,48 187,82 207,82 227,97 242,90 270,99 292,70 312,70 322,87 332,76 338,72" fill="none" stroke="#f1c983" stroke-width="1"/>
  <line x1="338" y1="0" x2="338" y2="144" stroke="#e8d7b5"/>
  <text x="4" y="30">1,000</text><text x="4" y="59">750</text><text x="4" y="89">550</text><text x="4" y="118">250</text>
  <text x="58" y="163">05 Apr</text><text x="103" y="163">10 Apr</text><text x="148" y="163">15 Apr</text>
  <text x="193" y="163">20 Apr</text><text x="238" y="163">25 Apr</text><text x="283" y="163">30 Apr</text>
</svg>

<h2 class="abs section-title" style="left:414px;top:599px">LATEST NEWS</h2>

<article class="abs news" style="top:651px">
  <div class="abs news-photo" role="img" aria-label="News photo of a smiling businessman" style="left:2px;top:5px"></div>
  <div class="abs news-date" style="left:60px;top:0"><span class="cal"></span>September,24</div>
  <div class="abs news-head" style="left:61px;top:13px;white-space:nowrap">Hasellus porta. Fusce suscipit</div>
  <div class="abs news-text" style="left:61px;top:25px;width:136px">India is fast catching up and the availability of power has a huge impact on the eco-</div>
  <div class="abs news-more" style="left:61px;top:47px">read more</div>
  <div class="abs" style="left:0;top:64px;width:194px;height:1px;background:var(--line)"></div>
</article>
<article class="abs news" style="top:744px">
  <div class="abs news-photo" role="img" aria-label="News photo of a smiling businessman" style="left:6px;top:4px"></div>
  <div class="abs news-date" style="left:64px;top:0"><span class="cal"></span>September,24</div>
  <div class="abs news-head" style="left:65px;top:12px;white-space:nowrap">Hasellus porta. Fusce suscipit</div>
  <div class="abs news-text" style="left:65px;top:24px;width:136px">India is fast catching up and the availability of power has a huge impact on the eco-</div>
  <div class="abs news-more" style="left:66px;top:46px">read more</div>
</article>

<h2 class="abs section-title" style="left:0;top:864px;width:656px;text-align:center">TESTIMONIALS</h2>

<blockquote class="abs quote" style="left:67px">Lorem ipsum dolor sit amet, consectetur adipisicing elit, sed do eiusmod tempor incididunt ut labore et</blockquote>
<blockquote class="abs quote" style="left:250px">Lorem ipsum dolor sit amet, consectetur adipisicing elit, sed do eiusmod tempor incididunt ut labore et</blockquote>
<blockquote class="abs quote" style="left:430px">Lorem ipsum dolor sit amet, consectetur adipisicing elit, sed do eiusmod tempor incididunt ut labore et</blockquote>

<div class="abs avatar" role="img" aria-label="Portrait of a customer" style="left:72px;top:957px"></div>
<div class="abs reviewer" style="left:110px;top:977px">Lorem ipsum</div>
<div class="abs avatar" role="img" aria-label="Portrait of a customer" style="left:252px;top:956px"></div>
<div class="abs reviewer" style="left:295px;top:975px">Lorem ipsum</div>
<div class="abs avatar" role="img" aria-label="Portrait of a customer" style="left:431px;top:956px"></div>
<div class="abs reviewer" style="left:471px;top:975px">Lorem ipsum</div>

<footer class="abs site-footer"></footer>
<div class="abs foot-col" style="left:61px">
  <h4>My Account</h4>
  <ul><li>My Account</li><li>Order History</li><li>Wish List</li><li>Newsletter</li><li>Delivery</li></ul>
</div>
<div class="abs foot-col" style="left:178px">
  <h4>Information</h4>
  <ul><li>About Us</li><li>Delivery Information</li><li>Privacy Policy</li><li>Terms &amp; Conditions</li><li>Refund Policy</li></ul>
</div>
<div class="abs foot-col" style="left:309px;top:1050px">
  <h4>Support</h4>
  <ul><li>Online Help</li><li>Community</li><li>Quick Start Guide (PDF)</li><li>User Guide (PDF)</li><li>F.A.Q</li></ul>
</div>
<div class="abs foot-col" style="left:429px;top:1052px">
  <h4 style="font-weight:400;width:158px">Social Networks</h4>
  <p class="social-note">Follow us on the social network sites Lorem ipsum dolor sit amet, consectetur adipisicing</p>
</div>
<div class="abs social"><i></i><i></i><i></i><i></i><i></i><i class="hot"></i><i></i></div>

<div class="abs legal">© Copyright websitename . All Rights Reserved &nbsp;&nbsp;&nbsp; Home | Contact | RSS</div>

</body>
</html>
```